Employees at R&T Gale Power Services need new modern business cards

We need new business cards that showcase our new rebranded logo. We are seeking modern, clean, fresh, attractive cards while still being professional. We want to stand out. A little bit about us: we work in Canada and the USA. We offer Technical Field Advisors to support wind turbine manufacturers through the construction phase of wind farms. I am attaching a mock inspiration picture to lead you in the direction we want to see this go. Also, FYI We have approx. 10/11 different employees that would need their own card. Let me know when you would need everyone's name. We would love to see some black and white options as well as color copies- when using colors we want green to be the dominant color with accents for blue and orange (colors should match our logo). I have also attached copies of our old business card for reference.

Contact Information for Business Card

Name, Telephone, Email, address, company name, website. EXAMPLE: Dean Whitlock, DeanWhitlock@randtgale.net, 555-384-9162, 318276 Fallow Line #7, Marrowby, ON X9Z 4Q2, www.randtgale.net

Colors
0054AA
0677BA
7BADD7
CADEEF
E8F1F8
00AB8E
00BBA5
67D7C9
C6EFE9
E9F9F6
F0912C
F2A743
F7CA91
FBE8D2
FDF5EE

Requirements
Must have
• 2 sided business card

```html
<!DOCTYPE html>
<html lang="en">
<head>
<meta charset="utf-8">
<title>R&amp;T Gale Power Services – Business Card</title>
<link rel="stylesheet" href="https://fonts.googleapis.com/css2?family=Arimo:wght@400;700&display=swap">
<style>
  :root {
    --backdrop: #e4e4e4;
    --card: #353535;
    --card-edge: #3d3d3d;
    --green: #3aae4a;
    --green-soft: #2f5b36;
    --orange: #f0912c;
    --text: #f2f2f2;
  }
  * { box-sizing: border-box; margin: 0; padding: 0; }
  html, body {
    width: 1200px; height: 1200px; overflow: hidden;
    background: var(--backdrop);
    font-family: "Arimo", Arial, sans-serif;
  }
  .card {
    position: absolute;
    left: 257px;
    width: 686px; height: 392px;
    border-radius: 22px;
    background: linear-gradient(160deg, var(--card-edge), var(--card));
    overflow: hidden;
  }
  .card--front { top: 165px; }
  .card--back { top: 653px; }

  .company-name {
    font-weight: 700;
    color: var(--green);
    letter-spacing: 0.02em;
  }
  .card--front .company-name {
    position: absolute; left: 58px; top: 78px;
    font-size: 27px; line-height: 1.1; width: 300px;
  }
  .person-name {
    position: absolute; left: 58px; top: 192px;
    font-size: 22px; font-weight: 700; color: var(--green);
  }
  .address {
    position: absolute; left: 58px; top: 233px;
    font-size: 15.5px; line-height: 19px; color: var(--text);
  }
  .contacts {
    position: absolute; left: 58px; top: 284px;
    list-style: none; font-size: 15.5px; color: var(--text);
  }
  .contacts li { display: flex; align-items: center; height: 19.5px; }
  .contacts svg { width: 14px; height: 14px; margin-right: 9px; fill: var(--orange); }

  .accent-circle {
    position: absolute; left: 375px; top: 20px;
    width: 352px; height: 352px; border-radius: 50%;
    background: var(--green-soft);
  }

  .back-brand {
    position: absolute; inset: 0;
    display: flex; flex-direction: column; align-items: center; justify-content: center;
    gap: 26px;
  }
  .brand-dot {
    width: 120px; height: 120px; border-radius: 50%;
    background: var(--green);
  }
  .card--back .company-name { font-size: 33px; }
</style>
</head>
<body>
  <section class="card card--front">
    <div class="accent-circle" role="img" aria-label="Brand symbol area"></div>
    <h1 class="company-name">R&amp;T Gale Power Services</h1>
    <p class="person-name">Dean Whitlock</p>
    <p class="address">318276 Fallow Line #7<br>Marrowby, ON X9Z 4Q2</p>
    <ul class="contacts">
      <li>
        <svg viewBox="0 0 24 24" aria-hidden="true"><path d="M6.6 10.8a15.1 15.1 0 0 0 6.6 6.6l2.2-2.2a1 1 0 0 1 1-.25 11.4 11.4 0 0 0 3.6.57 1 1 0 0 1 1 1V20a1 1 0 0 1-1 1A17 17 0 0 1 3 4a1 1 0 0 1 1-1h3.5a1 1 0 0 1 1 1c0 1.25.2 2.45.57 3.57a1 1 0 0 1-.25 1z"/></svg>
        555-384-9162
      </li>
      <li>
        <svg viewBox="0 0 24 24" aria-hidden="true"><path d="M2 5h20v14H2z M2 5l10 8 10-8" fill="var(--orange)"/><path d="M3 6l9 7 9-7" fill="none" stroke="#353535" stroke-width="1.6"/></svg>
        DeanWhitlock@randtgale.net
      </li>
      <li>
        <svg viewBox="0 0 24 24" aria-hidden="true"><circle cx="12" cy="12" r="10"/><path d="M2 12h20M12 2c3 3 3 17 0 20M12 2c-3 3-3 17 0 20" fill="none" stroke="#353535" stroke-width="1.4"/></svg>
        www.randtgale.net
      </li>
    </ul>
  </section>

  <section class="card card--back">
    <div class="back-brand">
      <div class="brand-dot" aria-hidden="true"></div>
      <h2 class="company-name">R&amp;T Gale Power Services</h2>
    </div>
  </section>
</body>
</html>
```